photowall advertisement

We require a wall featuring our company logo. We would like to avoid the color green, and gold is highly preferred. The design should be similar to the one in the attached photo. The wall will be used for photos and promotional purposes during congresses. Files must be prepared for printing.
dimension of wall: 470x223 cm

Industry/Entity Type

lifestyle

Colors
0054AA
0677BA
7BADD7
CADEEF
E8F1F8
6B429C
8869AF
B7A5CE
E3DAEB
F3F0F8

Requirements
Must have
• gold color, white, and other compare with gold color
Nice to have
• some pictograms, maps of Europe

```html
<!DOCTYPE html>
<html lang="en">
<head>
<meta charset="utf-8">
<title>Nova Crest Systems – Photo Wall</title>
<link rel="stylesheet" href="https://fonts.googleapis.com/css2?family=Poppins:wght@400;600;700&display=swap">
<style>
  :root {
    --white: #ffffff;
    --ink: #0b0b0b;
    --band: #000000;
    --map-grey: #e6e6e6;
    --gold-deep: #fdb32a;
    --gold-light: #fdd78a;
    --gold-mid: #f0a535;
    --gold-warm: #fbc94f;
    --bronze: #a85a1f;
  }
  html, body {
    margin: 0;
    padding: 0;
    width: 1200px;
    height: 566px;
    overflow: hidden;
    background: var(--white);
  }
  .photowall {
    position: relative;
    width: 1200px;
    height: 566px;
    font-family: "Poppins", sans-serif;
  }
  .logo-field {
    position: absolute;
    left: 0;
    width: 1200px;
  }
  .logo-field--white {
    top: 0;
    height: 246px;
    background: var(--white);
  }
  .logo-field--gold {
    top: 302px;
    height: 264px;
    background: linear-gradient(90deg,
      var(--gold-deep) 0%,
      var(--gold-deep) 8%,
      var(--gold-light) 30%,
      var(--gold-mid) 50%,
      var(--gold-light) 66%,
      var(--gold-warm) 88%,
      var(--bronze) 100%);
  }
  .europe-map {
    position: absolute;
    left: 20px;
    top: 0;
    width: 1160px;
    height: 246px;
  }
  .brand {
    position: absolute;
    display: flex;
    align-items: center;
    gap: 8px;
    transform: translateY(-50%);
    white-space: nowrap;
  }
  .brand__mark {
    width: 22px;
    height: 22px;
    background: var(--ink);
  }
  .brand__name {
    font-weight: 600;
    font-size: 20px;
    letter-spacing: 1px;
    color: var(--ink);
    text-transform: uppercase;
  }
  .web-band {
    position: absolute;
    left: 0;
    top: 246px;
    width: 1200px;
    height: 56px;
    background: var(--band);
  }
  .web-address {
    position: absolute;
    top: 50%;
    transform: translate(-50%, -50%);
    color: var(--white);
    font-size: 20px;
    font-weight: 400;
    white-space: nowrap;
  }
  .web-address strong { font-weight: 700; }
</style>
</head>
<body>
<main class="photowall">

  <section class="logo-field logo-field--white">
    <svg class="europe-map" role="img" aria-label="Faint grey map of Europe in the background" viewBox="0 0 1160 246">
      <defs>
        <radialGradient id="mapTone" cx="50%" cy="50%" r="50%">
          <stop offset="0%" stop-color="#e4e4e4" stop-opacity="0.8"/>
          <stop offset="100%" stop-color="#ffffff" stop-opacity="0"/>
        </radialGradient>
      </defs>
      <ellipse cx="380" cy="140" rx="330" ry="130" fill="url(#mapTone)"/>
      <ellipse cx="880" cy="130" rx="300" ry="130" fill="url(#mapTone)"/>
    </svg>

    <div class="brand" style="left:93px;top:23px"><span class="brand__mark"></span><span class="brand__name">Nova Crest Systems</span></div>
    <div class="brand" style="left:473px;top:23px"><span class="brand__mark"></span><span class="brand__name">Nova Crest Systems</span></div>
    <div class="brand" style="left:854px;top:23px"><span class="brand__mark"></span><span class="brand__name">Nova Crest Systems</span></div>

    <div class="brand" style="left:264px;top:86px"><span class="brand__mark"></span><span class="brand__name">Nova Crest Systems</span></div>
    <div class="brand" style="left:684px;top:86px"><span class="brand__mark"></span><span class="brand__name">Nova Crest Systems</span></div>

    <div class="brand" style="left:98px;top:149px"><span class="brand__mark"></span><span class="brand__name">Nova Crest Systems</span></div>
    <div class="brand" style="left:447px;top:149px"><span class="brand__mark"></span><span class="brand__name">Nova Crest Systems</span></div>
    <div class="brand" style="left:850px;top:149px"><span class="brand__mark"></span><span class="brand__name">Nova Crest Systems</span></div>

    <div class="brand" style="left:264px;top:219px"><span class="brand__mark"></span><span class="brand__name">Nova Crest Systems</span></div>
    <div class="brand" style="left:684px;top:219px"><span class="brand__mark"></span><span class="brand__name">Nova Crest Systems</span></div>
  </section>

  <section class="web-band">
    <span class="web-address" style="left:199px">www.<strong>NovaCrestSystems</strong>.com</span>
    <span class="web-address" style="left:600px">www.<strong>NovaCrestSystems</strong>.com</span>
    <span class="web-address" style="left:1002px">www.<strong>NovaCrestSystems</strong>.com</span>
  </section>

  <section class="logo-field logo-field--gold">
    <div class="brand" style="left:93px;top:32px"><span class="brand__mark"></span><span class="brand__name">Nova Crest Systems</span></div>
    <div class="brand" style="left:473px;top:32px"><span class="brand__mark"></span><span class="brand__name">Nova Crest Systems</span></div>
    <div class="brand" style="left:854px;top:32px"><span class="brand__mark"></span><span class="brand__name">Nova Crest Systems</span></div>

    <div class="brand" style="left:264px;top:96px"><span class="brand__mark"></span><span class="brand__name">Nova Crest Systems</span></div>
    <div class="brand" style="left:684px;top:96px"><span class="brand__mark"></span><span class="brand__name">Nova Crest Systems</span></div>

    <div class="brand" style="left:98px;top:159px"><span class="brand__mark"></span><span class="brand__name">Nova Crest Systems</span></div>
    <div class="brand" style="left:447px;top:159px"><span class="brand__mark"></span><span class="brand__name">Nova Crest Systems</span></div>
    <div class="brand" style="left:850px;top:159px"><span class="brand__mark"></span><span class="brand__name">Nova Crest Systems</span></div>

    <div class="brand" style="left:264px;top:229px"><span class="brand__mark"></span><span class="brand__name">Nova Crest Systems</span></div>
    <div class="brand" style="left:684px;top:229px"><span class="brand__mark"></span><span class="brand__name">Nova Crest Systems</span></div>
  </section>

</main>
</body>
</html>
```